Milo Fenwick - Cinematographer

NEED:
I'm looking for a sleek, professional, modern business card that will give give the recipient the impression that they can trust their production will go smoothly by hiring me. I will bring creativity and knowledge to their shoot, so that we can create powerful images.
I am looking for a card with a strong style and design ethos that could be expanded to a website and a full visual/graphic/design entity for me.
ABOUT ME:
I am a mid-twenties cinematographer, I work on music video, narrative short, commercial, and corporate projects. I blend the science and artistry of cameras and filmmaking to tell a story. I'm an artist, a technician, and a manager.
DESIGN:
I like sleek, simple design. Black, dark grays, white, dark navy, steel blues, I love cyan, but also cyan and red. I am not a fan of earthy tones. I generally prefer modern, san-serif fonts over serifs. My old logo was based on an aperture, a multi-blade device at the back of a lens that controls how much light passes through, but I made it with so many colors, that it doesn't necessarily lend itself to a specific color-scheme or design ethos. I liked that the aperture design provided a sense of the technical requirements of my job. I'm a fan of matte business cards, but am open to plenty of specialty print processes to make an outstanding card.
ATTACHED FILES:
My Old Rainbox Aperture Logo, plus a few designs I've tried playing around with, but am not tied to. I AM OPEN TO NEW DESIGNS, DO NOT FEEL TIED TO THIS.
**I've pulled my old logo down from the attached files, and instead attached other business cards I like, so as not to mislead you where I would like to go.
INFO:
Name: Milo Fenwick
Job: Cinematographer
Email: mpfenwick@quellbox.net
Phone: 415.555.0193
Website: milofenwick.net
I'm adding some images of other cards that I like, and removing my old logo, since I'm looking for something new, and don't want that old logo to push anyone a certain direction.

```html
<!DOCTYPE html>
<html lang="en">
<head>
<meta charset="utf-8">
<title>Milo Fenwick – Cinematographer Business Card</title>
<link rel="stylesheet" href="https://fonts.googleapis.com/css2?family=PT+Sans+Narrow:wght@400;700&family=Share+Tech+Mono&family=Open+Sans:ital,wght@1,300&display=swap">
<style>
  :root {
    --paper: #ffffff;
    --card-black: #060708;
    --disc-dark: #1a1b1b;
    --disc-mid: #2f3030;
    --name-white: #ffffff;
    --title-grey: #8a8a8a;
    --cyan: #1b8fd2;
    --stripe-red: #e5232b;
    --stripe-grey: #4a4a4a;
  }
  * { margin: 0; padding: 0; box-sizing: border-box; }
  html, body {
    width: 1200px; height: 933px; overflow: hidden;
    background: var(--paper);
  }
  .sheet { position: relative; width: 1200px; height: 933px; }
  .card {
    position: absolute; top: 0; width: 534px; height: 933px;
    background: var(--card-black); overflow: hidden;
  }
  .card--front { left: 0; }
  .card--back { left: 666px; }
  .card__art { position: absolute; inset: 0; }

  .front-name {
    position: absolute; left: 46px; top: 806px; width: 440px;
    font-family: "PT Sans Narrow", sans-serif; font-weight: 700;
    font-size: 66px; line-height: 1; color: var(--name-white);
    letter-spacing: -0.5px; text-transform: uppercase; white-space: nowrap;
  }
  .front-title {
    position: absolute; left: 116px; top: 866px;
    font-family: "Open Sans", sans-serif; font-style: italic; font-weight: 300;
    font-size: 31px; line-height: 1; letter-spacing: 8px;
    color: var(--title-grey); text-transform: uppercase; white-space: nowrap;
  }

  .back-text {
    position: absolute; left: 0; width: 534px; text-align: center;
    font-family: "Share Tech Mono", monospace; color: var(--cyan);
    white-space: nowrap; line-height: 1;
  }
  .back-name { top: 606px; font-size: 46px; letter-spacing: 9px; font-variant: small-caps; }
  .back-title { top: 664px; font-size: 36px; letter-spacing: 6px; font-variant: small-caps; }
  .back-email { top: 747px; font-size: 29px; letter-spacing: 4px; text-transform: uppercase; }
  .back-phone { top: 787px; font-size: 36px; letter-spacing: 4px; }
  .back-web { top: 858px; font-size: 29px; letter-spacing: 6px; text-transform: uppercase; }

  .stripe { position: absolute; left: 0; width: 534px; }
  .stripe--red-top { top: 704px; height: 6px; background: var(--stripe-red); }
  .stripe--grey { top: 715px; height: 9px; background: var(--stripe-grey); }
  .stripe--red-bottom { top: 731px; height: 6px; background: var(--stripe-red); }
</style>
</head>
<body>
<main class="sheet">
  <section class="card card--front">
    <svg class="card__art" width="534" height="933" viewBox="0 0 534 933">
      <circle cx="276" cy="142" r="262" fill="var(--disc-dark)" role="img" aria-label="Large faint camera aperture motif"/>
      <circle cx="298" cy="850" r="187" fill="var(--disc-mid)" role="img" aria-label="Camera aperture motif behind the name"/>
    </svg>
    <h1 class="front-name">Milo Fenwick</h1>
    <p class="front-title">Cinematographer</p>
  </section>

  <section class="card card--back">
    <svg class="card__art" width="534" height="933" viewBox="0 0 534 933">
      <circle cx="276" cy="142" r="262" fill="var(--disc-dark)" role="img" aria-label="Large faint camera aperture motif"/>
    </svg>
    <h2 class="back-text back-name">Milo Fenwick</h2>
    <p class="back-text back-title">Cinematographer</p>
    <div class="stripe stripe--red-top"></div>
    <div class="stripe stripe--grey"></div>
    <div class="stripe stripe--red-bottom"></div>
    <p class="back-text back-email">mpfenwick@quellbox.net</p>
    <p class="back-text back-phone">p. 415.555.0193</p>
    <p class="back-text back-web">www.milofenwick.net</p>
  </section>
</main>
</body>
</html>
```